K&R Security Services PTY. LTD.

Ive just had my logo made and I'm looking for some simple but strong designs for my business cards the company is a security company.

Please use dark colors.

Regards,

Owen Deloit

Reason: Need more time for discussion with other directors

Industry/Entity Type

Security

Font styles to use
Sans Serif
Decorative

```html
<!DOCTYPE html>
<html lang="en">
<head>
<meta charset="utf-8">
<title>K&amp;R Security Services – Business Card</title>
<link rel="stylesheet" href="https://fonts.googleapis.com/css2?family=Open+Sans:wght@300;400;600&display=swap">
<style>
  :root {
    --page: #3a3638;
    --frame: #b8b5b5;
    --frame-light: #d6d4d4;
    --panel: #f4f4f4;
    --panel-stripe: #ebebeb;
    --charcoal: #2e2b2c;
    --ink: #2a2a2a;
    --ink-soft: #4a4a4a;
  }
  * { margin: 0; padding: 0; box-sizing: border-box; }
  html, body {
    width: 1200px; height: 900px; overflow: hidden;
    background: var(--page);
    font-family: "Open Sans", sans-serif;
  }
  .canvas {
    position: relative; width: 1200px; height: 900px;
    display: flex; flex-direction: column; align-items: center; justify-content: center; gap: 40px;
  }
  .card {
    position: relative; width: 700px; height: 400px;
    border-radius: 14px; overflow: hidden;
    background: linear-gradient(135deg, var(--frame-light), var(--frame));
  }
  .card-shapes { position: absolute; inset: 0; width: 100%; height: 100%; }
  .brand {
    position: absolute; display: flex; align-items: center; gap: 10px;
    color: var(--charcoal); font-weight: 600; letter-spacing: 0.5px;
  }
  .brand-mark { background: var(--charcoal); flex: none; }
  .card-back .brand { left: 0; right: 0; top: 170px; justify-content: center; font-size: 34px; }
  .card-back .brand-mark { width: 34px; height: 34px; }
  .card-front .brand { left: 48px; top: 40px; font-size: 18px; }
  .card-front .brand-mark { width: 18px; height: 18px; }
  .holder { position: absolute; right: 58px; top: 150px; text-align: right; color: var(--ink); }
  .holder-name { font-size: 36px; font-weight: 300; letter-spacing: 1px; line-height: 1.1; }
  .holder-role { font-size: 13px; color: var(--ink-soft); }
  .contact { position: absolute; list-style: none; color: var(--ink); font-size: 13px; line-height: 1.55; }
  .contact li { display: flex; align-items: flex-start; gap: 10px; margin-bottom: 4px; }
  .contact svg { width: 13px; height: 13px; flex: none; margin-top: 3px; fill: var(--ink-soft); }
  .contact-location { left: 150px; top: 240px; }
  .contact-direct { left: 400px; top: 290px; }
</style>
</head>
<body>
<main class="canvas">

  <section class="card card-back" aria-label="Business card back">
    <svg class="card-shapes" viewBox="0 0 700 400" aria-hidden="true">
      <defs>
        <pattern id="stripes-back" width="6" height="6" patternUnits="userSpaceOnUse" patternTransform="rotate(45)">
          <rect width="6" height="6" fill="#f5f5f5"/><rect width="2" height="6" fill="#eeeeee"/>
        </pattern>
      </defs>
      <rect x="22" y="22" width="656" height="356" fill="url(#stripes-back)"/>
      <polygon points="560,0 700,0 700,120 678,120 678,22 600,22" fill="var(--charcoal)"/>
      <polygon points="0,270 22,270 22,378 110,378 140,400 0,400" fill="var(--charcoal)"/>
    </svg>
    <div class="brand"><span class="brand-mark"></span>K&amp;R Security Services</div>
  </section>

  <section class="card card-front" aria-label="Business card front">
    <svg class="card-shapes" viewBox="0 0 700 400" aria-hidden="true">
      <defs>
        <pattern id="stripes-front" width="6" height="6" patternUnits="userSpaceOnUse" patternTransform="rotate(45)">
          <rect width="6" height="6" fill="#f5f5f5"/><rect width="2" height="6" fill="#ebebeb"/>
        </pattern>
      </defs>
      <polygon points="16,16 684,16 684,384 170,384 16,150" fill="url(#stripes-front)"/>
      <polygon points="0,110 0,400 150,400" fill="var(--charcoal)"/>
      <polygon points="0,140 0,160 140,400 120,400" fill="var(--frame)"/>
      <polygon points="650,0 700,0 700,50 684,16 660,16" fill="var(--charcoal)"/>
      <polygon points="684,130 700,118 700,220 684,210" fill="var(--charcoal)"/>
    </svg>

    <div class="brand"><span class="brand-mark"></span>K&amp;R Security Services</div>

    <div class="holder">
      <p class="holder-name">OWEN DELOIT</p>
      <p class="holder-role">Security</p>
    </div>

    <ul class="contact contact-location">
      <li>
        <svg viewBox="0 0 16 16"><path d="M8 0a5.5 5.5 0 0 0-5.5 5.5C2.5 10 8 16 8 16s5.5-6 5.5-10.5A5.5 5.5 0 0 0 8 0zm0 8a2.5 2.5 0 1 1 0-5 2.5 2.5 0 0 1 0 5z"/></svg>
        <span>48 Harrow Lane,<br>Westbury NY 10492</span>
      </li>
      <li>
        <svg viewBox="0 0 16 16"><circle cx="8" cy="8" r="7" fill="none" stroke="#4a4a4a" stroke-width="1.6"/><path d="M1 8h14M8 1c-3 3.5-3 10.5 0 14M8 1c3 3.5 3 10.5 0 14" fill="none" stroke="#4a4a4a" stroke-width="1.2"/></svg>
        <span>www.krsecurity.example</span>
      </li>
    </ul>

    <ul class="contact contact-direct">
      <li>
        <svg viewBox="0 0 16 16"><path d="M3.5 1l3 3-1.8 1.8a9 9 0 0 0 5.5 5.5L12 9.5l3 3L13 15C6.5 14.5 1.5 9.5 1 3z"/></svg>
        <span>+(000) 555 0142</span>
      </li>
      <li>
        <svg viewBox="0 0 16 16"><rect x="4" y="1" width="8" height="5"/><rect x="1" y="7" width="14" height="6" rx="1"/><rect x="4" y="11" width="8" height="4" fill="#fff" stroke="#4a4a4a"/></svg>
        <span>+(000) 555 0143</span>
      </li>
      <li>
        <svg viewBox="0 0 16 16"><rect x="1" y="3" width="14" height="10" fill="none" stroke="#4a4a4a" stroke-width="1.5"/><path d="M1 3l7 6 7-6" fill="none" stroke="#4a4a4a" stroke-width="1.5"/></svg>
        <span>owen@krsecurity.example</span>
      </li>
    </ul>
  </section>

</main>
</body>
</html>
```